Business Card Design

The attached file is what i need on the front of the card. No details to be changed.

On the back could i have as a heading:
We buy for cash $$$
Deceased estates house lots
Antiques, vintage furniture, bikes, kitchenware, automobile, toys,
sports memorabilia, books, records, signage,farm equipment and fashion.

Industry/Entity Type

House

```html
<!DOCTYPE html>
<html lang="en">
<head>
<meta charset="utf-8">
<title>2718 Vintage – Business Card</title>
<link rel="stylesheet" href="https://fonts.googleapis.com/css2?family=Roboto+Condensed:wght@400;700&family=Anton&family=Lobster+Two:ital,wght@1,700&display=swap">
<style>
  :root {
    --page-bg: #eeeeee;
    --paper-light: #f4efdf;
    --paper-mid: #e9e0c6;
    --paper-dark: #cdbf98;
    --brand-red: #e3201f;
    --brand-red-deep: #b3161a;
    --ink: #232323;
    --ink-soft: #2e2e2e;
    --white: #ffffff;
  }
  * { margin: 0; padding: 0; box-sizing: border-box; }
  html, body {
    width: 1200px;
    height: 1150px;
    overflow: hidden;
    background: var(--page-bg);
    font-family: "Roboto Condensed", "Arial Narrow", sans-serif;
    color: var(--ink);
  }
  .canvas { position: relative; width: 1200px; height: 1150px; }

  .card {
    position: absolute;
    width: 750px;
    height: 472px;
    overflow: hidden;
  }
  .card-front { left: 147px; top: 85px; }
  .card-back  { left: 316px; top: 606px; }

  .paper-texture {
    position: absolute;
    inset: 0;
    background:
      radial-gradient(ellipse at 50% 45%, var(--paper-light) 0%, var(--paper-mid) 70%, var(--paper-dark) 100%);
  }

  .brush-band {
    position: absolute;
    background: radial-gradient(ellipse at 50% 50%, var(--brand-red) 60%, var(--brand-red-deep) 100%);
  }
  .card-front .brush-band { left: 15px; top: 28px; width: 720px; height: 300px; }
  .card-back  .brush-band { left: 18px; top: 45px; width: 720px; height: 66px; }

  .website-top {
    position: absolute;
    left: 0; right: 0; top: 30px;
    text-align: center;
    font-weight: 700;
    font-size: 22px;
    color: var(--ink);
  }
  .brand-name {
    position: absolute;
    left: 0; right: 0; top: 110px;
    text-align: center;
    font-weight: 700;
    font-size: 92px;
    line-height: 1;
    color: var(--ink);
  }
  .tagline {
    position: absolute;
    left: 0; right: 0; top: 284px;
    text-align: center;
    font-family: "Lobster Two", "Georgia", serif;
    font-style: italic;
    font-weight: 700;
    font-size: 29px;
    color: var(--white);
  }

  .contact {
    position: absolute;
    left: 17px; top: 348px;
    font-weight: 700;
    color: var(--ink);
  }
  .contact-line { font-size: 21px; line-height: 22px; }
  .contact-line .label { color: var(--brand-red); font-size: 18px; margin-right: 8px; }
  .contact-line.email { margin-top: 14px; font-size: 17px; }
  .contact-line.email .label { font-size: 17px; }
  .contact-line.address { margin-top: 6px; font-size: 17px; }

  .hours {
    position: absolute;
    left: 500px; width: 250px; top: 350px;
    text-align: center;
  }
  .hours-open {
    font-family: "Anton", "Impact", sans-serif;
    font-size: 26px;
    color: var(--brand-red);
    line-height: 1.1;
  }
  .hours-time { font-weight: 700; font-size: 23px; margin-top: 8px; }
  .hours-closed { font-weight: 700; font-size: 17px; margin-top: 6px; }

  .back-heading {
    position: absolute;
    left: 0; right: 0; top: 55px;
    text-align: center;
    font-weight: 700;
    font-size: 36px;
    color: var(--white);
  }
  .buy-list {
    position: absolute;
    left: 0; right: 0; top: 160px;
    text-align: center;
    font-weight: 700;
    font-size: 27px;
    line-height: 40px;
    color: var(--ink-soft);
  }
  .website-bottom {
    position: absolute;
    left: 0; right: 0; top: 420px;
    text-align: center;
    font-weight: 700;
    font-size: 24px;
    color: var(--brand-red);
  }
  .social-dot { position: absolute; left: 28px; top: 410px; }
</style>
</head>
<body>
<main class="canvas">

  <section class="card card-front" aria-label="Card front">
    <div class="paper-texture" role="img" aria-label="Aged, distressed cream paper texture"></div>
    <div class="brush-band" role="img" aria-label="Rough red painted brush stroke"></div>
    <p class="website-top">www.2718vintage.com.au</p>
    <h1 class="brand-name">2718 Vintage</h1>
    <p class="tagline">Vintage - Retro &nbsp;Clothing &amp; Collectables</p>

    <address class="contact">
      <p class="contact-line"><span class="label">p:</span>59 000 123</p>
      <p class="contact-line"><span class="label">m:</span>0400 555 218</p>
      <p class="contact-line email"><span class="label">e:</span>info@2718vintage.com.au</p>
      <p class="contact-line address">2718 Harbour Point Rd. Marlow 3999</p>
    </address>

    <div class="hours">
      <p class="hours-open">OPEN 6 DAYS A WEEK</p>
      <p class="hours-time">10:00am - 5:00pm</p>
      <p class="hours-closed">CLOSED TUESDAYS</p>
    </div>
  </section>

  <section class="card card-back" aria-label="Card back">
    <div class="paper-texture" role="img" aria-label="Aged, distressed cream paper texture"></div>
    <div class="brush-band" role="img" aria-label="Rough red painted brush stroke"></div>
    <h2 class="back-heading">WE BUY FOR CASH $$$</h2>
    <p class="buy-list">
      Deceased Estates House<br>
      Lots Antiques, Vintage Furniture,<br>
      Bikes, Kitchenware, Automobile, Toys,<br>
      Sports Memorabilia, Books, Records,<br>
      Signage, Farm Equipment And Fashion
    </p>
    <svg class="social-dot" width="54" height="54" viewBox="0 0 54 54" aria-hidden="true">
      <circle cx="27" cy="27" r="26" fill="var(--ink)"/>
    </svg>
    <p class="website-bottom">www.2718vintage.com.au</p>
  </section>

</main>
</body>
</html>
```